Hunting business needs poster design for trade shows

We need a poster designed that will be blown up to 78.7x33.5". that will be used as the main banner potential clients will see at trade shows. the poster sized banner will be blown up using 13 ounce super smooth grayback material.

Target Market(s)

Hunters. Outdoors

Industry/Entity Type

Hunting

Font styles to use
Serif

Colors
1b1b1b
474747
919191
757575
9d9d9d
eaeaea
ffffff
cbcbcb
aaaaaa

Requirements
Must have
• It must have my logo incorporated and the state of Illinois (an actual picture of it with the possibility of Scott and Morgan counties highlighted). Illinois needs to be the theme as that is a selling point. Like the document I attached, there should be 2 sections that feature archery hunting and firearm hunting that I circled as well as the bullet list. It also need Pennwood Ridge Outfitters and Est. 2005

```html
<!DOCTYPE html>
<html lang="en">
<head>
<meta charset="utf-8">
<title>Pennwood Ridge Outfitters – Trade Show Banner</title>
<link href="https://fonts.googleapis.com/css2?family=Source+Sans+3:wght@400;600;700&display=swap" rel="stylesheet">
<style>
  :root {
    --page-bg: #fcecc4;
    --ink: #1b1b1b;
    --ink-mid: #474747;
    --gray-dark: #474747;
    --gray-mid: #919191;
    --gray-soft: #cbcbcb;
    --gray-pale: #eaeaea;
    --white: #ffffff;
    --meadow-sky: #9fb3c4;
    --meadow-green: #8a9a3a;
    --meadow-deep: #3f4a1c;
  }
  * { box-sizing: border-box; margin: 0; padding: 0; }
  html, body { width: 720px; height: 1200px; overflow: hidden; }
  body {
    background: var(--page-bg);
    font-family: "Source Sans 3", "Myriad Pro", sans-serif;
    color: var(--ink);
    position: relative;
  }
  .banner {
    position: absolute;
    left: 122px; top: 33px;
    width: 476px; height: 1120px;
    background: var(--white);
    box-shadow: 3px 4px 8px rgba(0,0,0,0.25);
    overflow: hidden;
  }
  .hero-photo {
    position: absolute; left: 0; top: 0; width: 476px; height: 281px;
    background: linear-gradient(180deg, var(--meadow-sky) 0%, #c9c6a4 30%, var(--meadow-green) 55%, var(--meadow-deep) 100%);
  }
  .hero-arch {
    position: absolute; left: 0; top: 0;
  }
  .brand {
    position: absolute; left: 0; top: 300px; width: 476px;
    display: flex; justify-content: center; align-items: center; gap: 6px;
    font-weight: 600; font-size: 14px; letter-spacing: 1.5px;
    color: var(--ink);
    text-transform: uppercase;
  }
  .brand-dot {
    width: 8px; height: 8px; border-radius: 50%; background: var(--ink);
  }
  .content {
    position: absolute; left: 59px; width: 341px;
    font-size: 9.4px; line-height: 12.8px; color: var(--ink);
  }
  .content.archery { top: 353px; }
  .content.firearm { top: 578px; }
  .section-title { font-size: 13px; font-weight: 600; line-height: 16px; }
  .section-intro { text-align: justify; }
  .sub-title { font-weight: 600; margin-top: 11px; }
  .bullets { list-style: none; }
  .bullets li { position: relative; padding-left: 11px; }
  .bullets li::before { content: "•"; position: absolute; left: 0; }
  .divider {
    position: absolute; left: 38px; top: 559px; width: 389px; height: 1px;
    background: var(--ink-mid);
  }
  .field-photo {
    position: absolute; left: 0; top: 811px; width: 476px; height: 309px;
    background: linear-gradient(180deg, #dedede 0%, #c8c8c8 35%, #d8d8d8 70%, #bdbdbd 100%);
  }
  .diagonal-band { position: absolute; left: 0; top: 0; }
  .state-map {
    position: absolute; left: 286px; top: 795px; width: 162px; height: 292px;
    background: var(--gray-soft);
    border-radius: 6px;
  }
  .closing-title {
    position: absolute; left: 52px; top: 913px;
    font-size: 26px; font-weight: 700; line-height: 32px;
    color: var(--ink-mid);
  }
</style>
</head>
<body>
  <div class="banner">
    <div class="hero-photo" role="img" aria-label="Photograph of rolling green Illinois hills with a pond and trees under a bright sky"></div>
    <svg class="hero-arch" width="476" height="300" viewBox="0 0 476 300">
      <path d="M146 281 A92 92 0 0 1 330 281 Z" fill="var(--gray-pale)"/>
      <path d="M152 281 A86 86 0 0 1 324 281 Z" fill="var(--white)"/>
    </svg>
    <div class="brand"><span class="brand-dot"></span>Pennwood Ridge Outfitters</div>

    <section class="content archery">
      <h2 class="section-title">Archery Hunting</h2>
      <p class="section-intro">Pennwood Ridge specializes in guided archery hunts. Along with low hunter numbers, our work ethic, professionally hung and trimmed out stand locations, fail proof access routes and always taking the wind into consideration is what separates us from the competition.</p>
      <h3 class="sub-title">Pre-Rut and Rut Hunts</h3>
      <ul class="bullets">
        <li>Guided 5.5 day hunts that run from October 19 through November 14.</li>
        <li>Meals, lodging and guide services are included.</li>
        <li>No early season hunting</li>
      </ul>
      <h3 class="sub-title">Post Rut Hunts</h3>
      <ul class="bullets">
        <li>Semi-guided 6.5 day hunts that run from December 18 through January 14</li>
        <li>Late season food plots consist of corn, soybeans and brassicas.</li>
        <li>Farms are rested over a month before our late season hunts start.</li>
      </ul>
    </section>

    <div class="divider"></div>

    <section class="content firearm">
      <h2 class="section-title">Firearm Hunting</h2>
      <p class="section-intro">Pennwood Ridge offers a very limited number of shotgun / muzzleloader hunts that are spaced out over our 3 gun seasons. Blinds and elevated stands are our primary method of hunting and as always a low pressure strategy is in play.</p>
      <h3 class="sub-title">Firearm Seasons</h3>
      <ul class="bullets">
        <li>The first 3 day season capitalizes on rut hunting</li>
        <li>The second 4 day season is a day longer in length and focuses on food.</li>
        <li>The late muzzleloader only season is centered around food.</li>
      </ul>
      <h3 class="sub-title">Combo Firearm / Bow Hunts</h3>
      <ul class="bullets">
        <li>Guided 3.5 or 5.5 day archery hunts coupled with 3-4 days of firearm hunting.</li>
        <li>Non-residents are allowed to harvest 2 bucks (one with each weapon).</li>
      </ul>
    </section>

    <div class="field-photo" role="img" aria-label="Soft grayscale photograph of open Illinois farmland"></div>
    <svg class="diagonal-band" width="476" height="1120" viewBox="0 0 476 1120">
      <polygon points="476,707 476,1120 354,1120 278,895" fill="var(--gray-dark)"/>
    </svg>
    <div class="state-map" role="img" aria-label="Map of Illinois with Morgan and Scott counties highlighted"></div>
    <h2 class="closing-title">Archery Hunting<br>&amp; Firearm Hunting</h2>
  </div>
</body>
</html>
```